Business Card Design

We need a business card simular to the previous but including our logo our colours are royal blue, silver and black. we currently need cards for
Doug Pemberley Sales Manager 0400 295 617
doug@ridgelinegatesystems.com.au
Renee Blackwater 0415 832 190
renee@ridgelinegatesystems.com.au
Address 7 / 4 Marunga St Lonsdale
WEB www.ridgelinegatesystems.com.au
PH 84157203 Fax: 84157219
Updates
Good Morning all, I really don't like so much white. On the back I would like a list of all our products Security Doors & Screens, Built in Robes, Shower Screens, Blinds, Awnings, Roller Shutters & More Appointment Date & Time. Cheers Renee
Industry/Entity Type
Royal
Contact Information for Business Card
I really like the writing on our last business card from Cardmill.
Ridgeline Gate Systems , Factory Direct Prices, No Obligation Free Measure & Quote. List of Products Security Doors & Windows, Built in Robes, Indoor & Outdoor Blinds Inc Awnings & Velafolds, Shower Screens, Roller Shutters and More.
Font styles to use

```html
<!DOCTYPE html>
<html lang="en">
<head>
<meta charset="utf-8">
<title>Ridgeline Gate Systems – Business Card</title>
<link href="https://fonts.googleapis.com/css2?family=Open+Sans:wght@400;600;700;800&display=swap" rel="stylesheet">
<style>
  :root {
    --royal: #1f5fae;
    --ink: #3a3a3a;
    --ink-soft: #555;
    --paper: #ffffff;
    --stage: #a4a4a4;
  }
  * { box-sizing: border-box; margin: 0; padding: 0; }
  html, body { width: 1200px; height: 896px; overflow: hidden; }
  body {
    background: var(--stage);
    font-family: "Open Sans", Arial, sans-serif;
    position: relative;
  }
  .card {
    position: absolute;
    width: 620px;
    height: 354px;
    background: var(--paper);
    box-shadow: 0 8px 22px rgba(0,0,0,.28);
    overflow: hidden;
  }
  .card-back { left: 520px; top: 70px; }
  .card-front { left: 60px; top: 470px; }
  .swoosh { position: absolute; left: 0; width: 100%; }
  .swoosh-top { top: 0; }
  .swoosh-bottom { bottom: 0; }
  .brand {
    position: absolute;
    display: flex;
    align-items: center;
    gap: 12px;
    font-weight: 800;
    color: var(--royal);
    line-height: 1;
    white-space: nowrap;
  }
  .brand-mark { display: block; background: var(--royal); }
  .card-back .brand { left: 0; right: 0; justify-content: center; top: 112px; font-size: 34px; }
  .card-back .brand-mark { width: 34px; height: 34px; }
  .card-front .brand { left: 40px; top: 40px; font-size: 27px; }
  .card-front .brand-mark { width: 28px; height: 28px; }
  .products {
    position: absolute;
    left: 40px; right: 40px; top: 206px;
    list-style: none;
    display: flex;
    flex-wrap: wrap;
    justify-content: center;
    gap: 10px 26px;
    font-size: 14px;
    color: var(--ink-soft);
  }
  .product { display: flex; align-items: center; gap: 9px; white-space: nowrap; }
  .product-dot { width: 14px; height: 14px; background: var(--royal); display: block; flex: none; }
  .edge-tab { position: absolute; background: var(--royal); }
  .card-back .edge-tab { right: 0; top: 160px; width: 18px; height: 38px; }
  .card-front .edge-tab { left: 0; top: 104px; width: 24px; height: 46px; }
  .holder { position: absolute; left: 44px; top: 104px; }
  .holder-name {
    font-size: 27px; font-weight: 800; color: var(--ink);
    letter-spacing: .5px; text-transform: uppercase; line-height: 1.1;
  }
  .holder-role {
    font-size: 13px; font-weight: 400; color: var(--royal);
    letter-spacing: 5px; text-transform: uppercase; margin-top: 2px;
  }
  .contacts {
    position: absolute; left: 318px; top: 226px;
    list-style: none;
    font-size: 13px; font-weight: 600; color: var(--ink);
    line-height: 1.25;
    white-space: nowrap;
  }
  .contacts li { display: flex; align-items: flex-start; gap: 12px; margin-bottom: 9px; }
  .contacts svg { flex: none; width: 16px; height: 16px; margin-top: 1px; }
</style>
</head>
<body>

<section class="card card-back" aria-label="Business card back">
  <svg class="swoosh swoosh-top" viewBox="0 0 620 40" height="40" preserveAspectRatio="none" aria-hidden="true">
    <path d="M0,0 H620 V22 Q380,4 0,3 Z" fill="var(--royal)"/>
  </svg>
  <div class="brand"><span class="brand-mark"></span>Ridgeline Gate Systems</div>
  <ul class="products">
    <li class="product"><span class="product-dot"></span>Security Doors &amp; Screens</li>
    <li class="product"><span class="product-dot"></span>Built in Robes</li>
    <li class="product"><span class="product-dot"></span>Shower Screens</li>
    <li class="product"><span class="product-dot"></span>Blinds</li>
    <li class="product"><span class="product-dot"></span>Awnings</li>
    <li class="product"><span class="product-dot"></span>Roller Shutters &amp; More</li>
  </ul>
  <span class="edge-tab"></span>
  <svg class="swoosh swoosh-bottom" viewBox="0 0 620 40" height="40" preserveAspectRatio="none" aria-hidden="true">
    <path d="M0,40 H620 V36 Q300,36 0,18 Z" fill="var(--royal)"/>
  </svg>
</section>

<section class="card card-front" aria-label="Business card front">
  <svg class="swoosh swoosh-top" viewBox="0 0 620 40" height="40" preserveAspectRatio="none" aria-hidden="true">
    <path d="M0,0 H620 V3 Q300,6 0,26 Z" fill="var(--royal)"/>
  </svg>
  <div class="brand"><span class="brand-mark"></span>Ridgeline Gate Systems</div>
  <span class="edge-tab"></span>
  <div class="holder">
    <p class="holder-name">Doug Pemberley</p>
    <p class="holder-role">Sales Manager</p>
  </div>
  <ul class="contacts">
    <li>
      <svg viewBox="0 0 16 16" aria-hidden="true"><path d="M8 1.5 1 8h2v6.5h4v-4h2v4h4V8h2z" fill="var(--royal)"/></svg>
      <span>7 / 4 Marunga St<br>Lonsdale</span>
    </li>
    <li>
      <svg viewBox="0 0 16 16" aria-hidden="true" fill="none" stroke="var(--royal)" stroke-width="1.4"><circle cx="8" cy="8" r="6.3"/><ellipse cx="8" cy="8" rx="2.8" ry="6.3"/><path d="M1.7 8h12.6M2.8 4.8h10.4M2.8 11.2h10.4"/></svg>
      <span>www.ridgelinegatesystems.com.au</span>
    </li>
    <li>
      <svg viewBox="0 0 16 16" aria-hidden="true"><rect x="1" y="3.5" width="14" height="9" fill="var(--royal)"/><path d="M1.5 4 8 9l6.5-5" fill="none" stroke="#fff" stroke-width="1.2"/></svg>
      <span>doug@ridgelinegatesystems.com.au</span>
    </li>
    <li>
      <svg viewBox="0 0 16 16" aria-hidden="true"><path d="M4 1.5 6.3 4.3 5 6c.8 1.9 2.2 3.3 4 4.2l1.7-1.3 2.8 2.3-1.4 2.3C7 13.3 2.6 8.9 1.7 3z" fill="var(--royal)"/></svg>
      <span>0400 295 617</span>
    </li>
  </ul>
</section>

</body>
</html>
```